" Montamos roteiros turisticos especializados em experiência. Inicialmente a empresa ofertará roteiros especializados para fotografia, porém no futuro poderá conter roteiros para vinhos, culinária, esportes, etc. "

```html
<!DOCTYPE html>
<html lang="pt-BR">
<head>
<meta charset="utf-8">
<title>Vivera — Quem Somos</title>
<link href="https://fonts.googleapis.com/css2?family=Open+Sans:wght@400;600;700&display=swap" rel="stylesheet">
<style>
  :root{
    --page-bg:#e9e9e7;
    --nav-bg:rgba(22,24,27,.92);
    --nav-text:#f2f2f2;
    --accent:#e8782c;
    --hero-text:#f4f1ec;
    --player-bar:#f7f7f7;
    --player-track:#c9c9c9;
    --player-progress:#e23c3c;
    --icon:#555;
    --video-top:#9ccfe4;
    --video-bottom:#5fb8bf;
  }
  *{box-sizing:border-box;margin:0;padding:0}
  html,body{width:1200px;height:1200px;overflow:hidden}
  body{background:var(--page-bg);font-family:"Open Sans",Arial,sans-serif;position:relative}

  .site{position:absolute;left:0;top:240px;width:1200px;height:720px;overflow:hidden}
  .hero-photo{position:absolute;inset:0;
    background:
      linear-gradient(rgba(20,16,12,.55),rgba(20,16,12,.55)),
      radial-gradient(ellipse at 85% 35%,#a0643a 0%,rgba(160,100,58,0) 45%),
      linear-gradient(180deg,#6b6a66 0%,#7a6450 35%,#8a6a40 60%,#6e5530 100%);}

  .nav{position:absolute;left:0;top:0;width:100%;height:78px;background:var(--nav-bg);
    display:flex;align-items:center;padding:0 40px}
  .brand{display:flex;align-items:center;gap:10px;color:#fff}
  .brand-dot{width:36px;height:36px;border-radius:50%;background:#2f8fd1}
  .brand-text{display:flex;flex-direction:column;line-height:1}
  .brand-name{font-size:32px;font-weight:600}
  .brand-tag{font-size:8px;letter-spacing:1.5px;margin-top:4px;font-weight:600}
  .menu{display:flex;gap:22px;margin-left:80px;list-style:none}
  .menu li{color:var(--nav-text);font-size:13px;font-weight:600;text-transform:uppercase;white-space:nowrap}
  .menu li.is-active{color:var(--accent)}
  .search{margin-left:auto}

  .intro{position:absolute;top:130px;left:0;width:100%;text-align:center;color:var(--hero-text)}
  .intro h1{font-size:17px;font-weight:400;letter-spacing:1px;text-transform:uppercase}
  .intro p{width:860px;margin:22px auto 0;font-size:22px;line-height:1.35;text-align:center}

  .video{position:absolute;left:370px;top:340px;width:460px;height:300px;background:#fff;
    box-shadow:0 4px 16px rgba(0,0,0,.4)}
  .video-still{position:absolute;left:0;top:0;width:100%;height:266px;
    background:linear-gradient(180deg,var(--video-top) 0%,var(--video-bottom) 100%)}
  .play{position:absolute;left:208px;top:112px;width:44px;height:44px;border-radius:50%;
    background:rgba(255,255,255,.92);display:flex;align-items:center;justify-content:center}
  .controls{position:absolute;left:0;bottom:0;width:100%;height:34px;background:var(--player-bar);
    display:flex;align-items:center;gap:10px;padding:0 12px;font-size:11px;color:#444}
  .track{flex:1;height:4px;background:var(--player-track);position:relative}
  .track::before{content:"";position:absolute;left:0;top:0;height:100%;width:18%;background:var(--player-progress)}
</style>
</head>
<body>
  <main class="site">
    <div class="hero-photo" role="img" aria-label="Paisagem de deserto com árvores secas, capim dourado e grandes rochas avermelhadas"></div>

    <header class="nav">
      <div class="brand">
        <span class="brand-dot"></span>
        <span class="brand-text">
          <span class="brand-name">Vivera</span>
          <span class="brand-tag">VIAGENS FOTOGRÁFICAS</span>
        </span>
      </div>
      <ul class="menu">
        <li>Home</li>
        <li class="is-active">Quem Somos</li>
        <li>Próximas Expedições</li>
        <li>Últimas Viagens</li>
        <li>Dúvidas</li>
        <li>Fale Conosco</li>
      </ul>
      <svg class="search" width="16" height="16" viewBox="0 0 16 16" aria-hidden="true">
        <circle cx="6.5" cy="6.5" r="5" fill="none" stroke="#fff" stroke-width="2"/>
        <line x1="10.3" y1="10.3" x2="15" y2="15" stroke="#fff" stroke-width="2"/>
      </svg>
    </header>

    <section class="intro">
      <h1>Conheça a Vivera</h1>
      <p>A Vivera tem como missão criar e oferecer roteiros turísticos para os apaixonados por fotografia, viabilizando toda logística necessária para o melhor aproveitamento dos momentos únicos proporcionados pela mãe natureza.</p>
    </section>

    <div class="video">
      <div class="video-still" role="img" aria-label="Quadro do vídeo: praia com água turquesa e montanhas ao fundo"></div>
      <div class="play">
        <svg width="16" height="18" viewBox="0 0 16 18" aria-hidden="true"><path d="M2 1 L15 9 L2 17 Z" fill="#333"/></svg>
      </div>
      <div class="controls">
        <svg width="10" height="12" viewBox="0 0 10 12" aria-hidden="true"><path d="M1 0 L10 6 L1 12 Z" fill="var(--icon)"/></svg>
        <span>2:16</span>
        <div class="track"></div>
        <svg width="14" height="12" viewBox="0 0 14 12" aria-hidden="true"><path d="M0 4 H3 L7 0 V12 L3 8 H0 Z" fill="var(--icon)"/><path d="M9 3 Q12 6 9 9" stroke="var(--icon)" fill="none" stroke-width="1.5"/></svg>
        <svg width="12" height="12" viewBox="0 0 12 12" aria-hidden="true"><circle cx="6" cy="6" r="4" fill="none" stroke="var(--icon)" stroke-width="2"/></svg>
        <svg width="12" height="12" viewBox="0 0 12 12" aria-hidden="true"><path d="M0 4V0H4M8 0H12V4M12 8V12H8M4 12H0V8" fill="none" stroke="var(--icon)" stroke-width="1.6"/></svg>
      </div>
    </div>
  </main>
</body>
</html>
```